NEW Escape Room. Fun, Dark and Mysterious.

Escape Room Website. Bookings and scheduling of appointments will be organised with Bookvane through the site. Most appointments will be created online through the booking system with some payments coming through in person by drop-ins. Groups will be from 2 - 8 people with a sliding scale of prices. We will start with one game playable and one saying coming soon. We will also eventually have 4 games up and running at once so will need it to be able to expand. We don't have any images of the rooms because it all relies heavily on mystery. Appointments are each 1 hour long with 30 minutes in between.

Target Market(s)

15-35 year olds

Coding

Coded - Design and coding required

Number of Pages Required

5+ page

Font styles to use
Decorative

Colors

Designer to choose colors to be used in the design.

Requirements
Must have
• Graphics showing what an escape room is.
• Page for About - What is an escape room
• Page for Games - Showing each of the different games which can be played with links to booking page. We have one game to start - the surgeons shadows. A victorian doctors office and serial killers. Then a game coming soon which is aztec/mayan/jungle/harold Crane feel.
• FAQ Page
Nice to have
• Graphics for multiple players ie 2 players, 3 players, 4 players etc
• Dark and Mysterious feel.
• Inspiration from Puzzle Vault, Cipher Lodge, Quest Lockbox
Should not have
• Cartoony/childish. Pink.
• Not bloody or dripping letters etc - not cliche.
• Not horror themed.

```html
<!DOCTYPE html>
<html lang="en">
<head>
<meta charset="utf-8">
<title>Games – Last Latch</title>
<link href="https://fonts.googleapis.com/css2?family=Poppins:wght@400;600;700;800&family=Open+Sans:wght@400&family=Montserrat:wght@500&display=swap" rel="stylesheet">
<style>
:root{
  --bg:#070708;
  --bar:#0b0b0d;
  --white:#ffffff;
  --text:#c9c9c9;
  --muted:#a9a9a9;
  --orange:#e5862a;
  --orange-dark:#c05f1c;
  --gold:#e8a33c;
  --star-off:#5a5a5a;
}
*{margin:0;padding:0;box-sizing:border-box}
html,body{width:748px;height:1200px;overflow:hidden;background:var(--bg)}
.page{position:relative;width:748px;height:1200px;overflow:hidden;
  background:
    radial-gradient(circle at 40px 380px, rgba(200,150,60,.16), transparent 130px),
    radial-gradient(circle at 730px 560px, rgba(200,150,60,.18), transparent 150px),
    radial-gradient(circle at 30px 720px, rgba(200,150,60,.10), transparent 110px),
    radial-gradient(circle at 700px 1180px, rgba(200,150,60,.14), transparent 110px),
    radial-gradient(circle at 120px 1190px, rgba(200,150,60,.10), transparent 120px),
    var(--bg);
  font-family:'Open Sans',sans-serif}
.nav{position:absolute;top:0;left:0;width:748px;height:42px;background:var(--bar);z-index:3}
.nav a,.foot-nav a{position:absolute;top:50%;transform:translate(-50%,-50%);font-family:'Poppins',sans-serif;font-weight:700;font-size:11px;color:var(--white);text-decoration:none;white-space:nowrap}
.nav a.active{color:var(--gold)}
.nav .sep{position:absolute;top:15px;width:1px;height:12px;background:#444}
.hero{position:absolute;top:0;left:0;width:748px;height:352px}
.hero-art{position:absolute;inset:0}
.brand{position:absolute;top:100px;left:0;width:748px;display:flex;justify-content:center;align-items:center;gap:8px;z-index:2}
.brand .mark{width:14px;height:14px;border-radius:50%;background:var(--orange)}
.brand span{font-family:'Poppins',sans-serif;font-weight:700;font-size:20px;color:var(--orange);letter-spacing:1px}
.hero h1{position:absolute;top:196px;left:0;width:748px;text-align:center;font-family:'Poppins',sans-serif;font-weight:800;font-size:40px;color:var(--white);z-index:2}
.game{position:absolute}
.hex{position:absolute}
.game h2{font-family:'Poppins',sans-serif;font-weight:700;font-size:19px;line-height:22px;color:var(--orange);text-transform:uppercase}
.game .soon{font-family:'Poppins',sans-serif;font-weight:400;font-size:15px;color:var(--orange-dark);line-height:20px}
.game p.desc{margin-top:10px;font-size:10px;line-height:15.5px;color:var(--text)}
.game .meta{font-family:'Montserrat',sans-serif;font-weight:500;font-size:10px;color:var(--white);letter-spacing:.3px}
.schedule{margin-top:14px}
.rating{margin-top:12px;display:flex;align-items:center;gap:6px}
.stars{display:flex;gap:2px}
.btn{display:block;margin-top:15px;width:132px;height:41px;border:1px solid var(--orange);padding:3px}
.btn span{display:flex;width:100%;height:100%;align-items:center;justify-content:center;background:linear-gradient(var(--orange),var(--orange-dark));font-family:'Poppins',sans-serif;font-weight:700;font-size:11px;letter-spacing:.8px;color:var(--white)}
.footer{position:absolute;left:0;top:1000px;width:748px;height:200px}
.foot-brand{position:absolute;top:55px;left:0;width:748px;display:flex;justify-content:center;align-items:center;gap:6px}
.foot-brand .mark{width:10px;height:10px;border-radius:50%;background:var(--orange)}
.foot-brand span{font-family:'Poppins',sans-serif;font-weight:700;font-size:14px;color:var(--orange)}
.foot-nav{position:absolute;top:104px;left:0;width:748px;height:20px}
.foot-nav a{color:var(--muted)}
.copy{position:absolute;top:130px;left:0;width:748px;text-align:center;font-family:'Poppins',sans-serif;font-size:8px;color:var(--muted)}
.social{position:absolute;top:151px;left:326px;display:flex;gap:2px}
.social i{display:block;width:22px;height:22px;border-radius:50%;border:1px solid var(--white)}
.social i:first-child{border-color:var(--orange)}
</style>
</head>
<body>
<div class="page">
  <nav class="nav">
    <a href="#" style="left:175px">HOME</a><i class="sep" style="left:216px"></i>
    <a href="#" style="left:263px">ABOUT</a><i class="sep" style="left:308px"></i>
    <a href="#" class="active" style="left:354px">GAMES</a><i class="sep" style="left:399px"></i>
    <a href="#" style="left:461px">CONTACT US</a><i class="sep" style="left:519px"></i>
    <a href="#" style="left:560px">FAQ</a>
  </nav>

  <header class="hero">
    <svg class="hero-art" width="748" height="352" viewBox="0 0 748 352">
      <defs>
        <linearGradient id="heroFill" x1="0" y1="0" x2="1" y2="1">
          <stop offset="0" stop-color="#3a3a3a"/><stop offset=".35" stop-color="#2a2a2b"/><stop offset="1" stop-color="#141415"/>
        </linearGradient>
        <radialGradient id="hatchLight" cx="220" cy="90" r="160" gradientUnits="userSpaceOnUse">
          <stop offset="0" stop-color="#9a9a9a" stop-opacity=".7"/><stop offset="1" stop-color="#9a9a9a" stop-opacity="0"/>
        </radialGradient>
      </defs>
      <g role="img" aria-label="Dark stone cell with a ladder climbing to a lit hatch">
        <polygon points="0,42 748,42 748,268 374,345 0,268" fill="url(#heroFill)"/>
        <polygon points="0,42 748,42 748,268 374,345 0,268" fill="url(#hatchLight)"/>
      </g>
      <polyline points="0,270 374,349 748,270" fill="none" stroke="#e5862a" stroke-width="2.5"/>
    </svg>
    <div class="brand"><i class="mark"></i><span>LAST LATCH</span></div>
    <h1>GAMES</h1>
  </header>

  <svg class="hex" style="left:123px;top:407px" width="212" height="244" viewBox="0 0 212 244" role="img" aria-label="Figure standing in a glowing keyhole doorway">
    <defs><linearGradient id="hexA" x1="0" y1="0" x2="1" y2="1"><stop offset="0" stop-color="#6b4a2c"/><stop offset=".4" stop-color="#d7a25c"/><stop offset="1" stop-color="#2a2530"/></linearGradient></defs>
    <polygon points="106,1 211,61 211,183 106,243 1,183 1,61" fill="none" stroke="#e5862a" stroke-width="1"/>
    <polygon points="106,9 204,65 204,179 106,235 8,179 8,65" fill="url(#hexA)"/>
  </svg>
  <section class="game" style="left:365px;top:432px;width:320px">
    <h2>Surgeons Shadows</h2>
    <p class="desc">Nunc tempus felis vitae urna Vivamus porttitor neque at volutpat rutrum purus nisi eleifend libero a tempus libero lectus feugiat felis Morbi diam mauris viverra in gravida eu mattis in ante Morbi eget arcu Morbi porta libero id ullamcorper nonu</p>
    <div class="meta schedule">Schedule available: 25 Feb to 28 Feb</div>
    <div class="meta rating">Difficulty Rating:
      <svg class="stars" width="80" height="14" viewBox="0 0 80 14">
        <defs><polygon id="star" points="7,0 8.7,4.8 13.7,4.9 9.7,7.9 11.2,12.8 7,9.9 2.8,12.8 4.3,7.9 0.3,4.9 5.3,4.8"/></defs>
        <use href="#star" fill="#e5862a"/><use href="#star" x="16" fill="#e5862a"/><use href="#star" x="32" fill="#e5862a"/><use href="#star" x="48" fill="#e5862a"/><use href="#star" x="64" fill="#5a5a5a"/>
      </svg>
    </div>
    <a href="#" class="btn"><span>BOOK NOW</span></a>
  </section>

  <section class="game" style="left:129px;top:757px;width:320px">
    <h2>Jaguar King's Tomb</h2>
    <div class="soon">(COMING SOON)</div>
    <p class="desc" style="margin-top:6px">Nunc tempus felis vitae urna Vivamus porttitor neque at volutpat rutrum purus nisi eleifend libero a tempus libero lectus feugiat felis Morbi diam mauris viverra in gravida eu mattis</p>
    <div class="meta schedule">Schedule available: 23 Feb to 25 Feb</div>
    <div class="meta rating">Difficulty Rating:
      <svg class="stars" width="80" height="14" viewBox="0 0 80 14">
        <defs><clipPath id="half"><rect x="48" y="0" width="7" height="14"/></clipPath></defs>
        <use href="#star" fill="#e5862a"/><use href="#star" x="16" fill="#e5862a"/><use href="#star" x="32" fill="#e5862a"/><use href="#star" x="48" fill="#5a5a5a"/><use href="#star" x="48" fill="#e5862a" clip-path="url(#half)"/><use href="#star" x="64" fill="#5a5a5a"/>
      </svg>
    </div>
    <a href="#" class="btn"><span>BOOK NOW</span></a>
  </section>
  <svg class="hex" style="left:458px;top:721px" width="212" height="244" viewBox="0 0 212 244" role="img" aria-label="Ancient stone chamber with a glowing orb over a carved floor circle">
    <defs><linearGradient id="hexB" x1="0" y1="0" x2="1" y2="1"><stop offset="0" stop-color="#b07a55"/><stop offset=".5" stop-color="#8a5a3c"/><stop offset="1" stop-color="#3b2418"/></linearGradient></defs>
    <polygon points="106,1 211,61 211,183 106,243 1,183 1,61" fill="none" stroke="#e5862a" stroke-width="1"/>
    <polygon points="106,9 204,65 204,179 106,235 8,179 8,65" fill="url(#hexB)"/>
  </svg>

  <footer class="footer">
    <svg width="748" height="200" viewBox="0 0 748 200" style="position:absolute;left:0;top:0">
      <polygon points="0,102 345,50 403,50 748,104 748,200 0,200" fill="#0e0e0f"/>
      <line x1="0" y1="102" x2="345" y2="50" stroke="#e5862a" stroke-width="1.5"/>
      <line x1="403" y1="50" x2="748" y2="104" stroke="#e5862a" stroke-width="1.5"/>
    </svg>
    <div class="foot-brand"><i class="mark"></i><span>LAST LATCH</span></div>
    <nav class="foot-nav">
      <a href="#" style="left:216px">HOME</a>
      <a href="#" style="left:290px">ABOUT</a>
      <a href="#" style="left:366px">GAMES</a>
      <a href="#" style="left:458px">CONTACT US</a>
      <a href="#" style="left:547px">FAQ</a>
    </nav>
    <div class="copy">© 2020 Company Name | All Rights Reserved | Disclaimer</div>
    <div class="social"><i></i><i></i><i></i><i></i></div>
  </footer>
</div>
</body>
</html>
```